New Business Card Design Project

Easy part first... I want the backside to be simple... jet black background with our logo in jet black/white/color. Feel free to play with tagline ideas under the logo if you want, I'm still toying around with it myself.

The front side... I need the logo on it, my photo headshot, and the following information:

Ray T. Dalworth
Top Producer
313-482-6157
dalworth.ray.t@mailnest.example
www.listlakeshorehomes.example
www.findlakeshorehomes.example

I'm looking for creativity with font, simple, but elegant, pairs well with the logo, good visibility of my photo, black background on the front as well, clearly see and identify information.
Updates

I would like the websites to have capitalization on the first letter of each word - www.ListLakeshoreHomes.example and www.FindLakeshoreHomes.example Also, I would like each of the capital letters to be slightly larger than the other font

Target Market(s)

We help people buy and sell homes from $50,000 to over a $1million.

Industry/Entity Type

Business

Requirements
Must have
• Must have information from above.
Nice to have
• Introducing a new color to be sharp against the black- possibly in the silver/nickel/platinum metallics? Feel free to crop the headshot down some if needed.
Should not have
• NO CHEESY GRAPHICS

```html
<!DOCTYPE html>
<html lang="en">
<head>
<meta charset="utf-8">
<title>Harbor Key Realty – Business Card</title>
<link rel="stylesheet" href="https://fonts.googleapis.com/css2?family=Open+Sans:wght@400;600&display=swap">
<style>
  :root {
    --canvas: #e9e6e1;
    --card-black: #050505;
    --card-white: #ffffff;
    --ink: #111111;
    --light: #f4f4f4;
    --photo-dark: #3a2c22;
    --photo-mid: #6b5446;
    --rule: #c9c9c9;
  }
  * { box-sizing: border-box; margin: 0; padding: 0; }
  html, body { width: 1200px; height: 1000px; overflow: hidden; }
  body {
    background: var(--canvas);
    font-family: "Open Sans", Arial, sans-serif;
    position: relative;
  }
  .card {
    position: absolute;
    width: 700px;
    height: 400px;
    left: 250px;
    box-shadow: 0 10px 30px rgba(0,0,0,.25);
    overflow: hidden;
  }
  .card--back { top: 50px; background: var(--card-black); display: flex; align-items: center; justify-content: center; }
  .card--front { top: 530px; display: flex; background: var(--card-black); }

  .brand { display: flex; align-items: center; gap: 14px; color: var(--light); font-weight: 600; text-transform: uppercase; letter-spacing: .12em; }
  .brand__mark { background: var(--light); flex: none; }
  .card--back .brand { font-size: 40px; }
  .card--back .brand__mark { width: 22px; height: 22px; }

  .front__id {
    width: 290px;
    flex: none;
    background: var(--card-white);
    padding: 34px 28px 0 30px;
    border-right: 3px solid var(--rule);
  }
  .front__photo {
    width: 232px;
    height: 236px;
    background: linear-gradient(160deg, var(--photo-mid), var(--photo-dark));
  }
  .front__name { margin-top: 14px; font-size: 29px; color: var(--ink); font-weight: 400; line-height: 1.1; }
  .front__title { font-size: 17px; color: var(--ink); letter-spacing: .06em; margin-top: 6px; }

  .front__info { flex: 1; min-width: 0; padding: 54px 18px 0 26px; color: var(--light); }
  .front__info .brand { font-size: 22px; justify-content: center; margin-bottom: 74px; }
  .front__info .brand__mark { width: 13px; height: 13px; }
  .contact { list-style: none; }
  .contact li { display: flex; align-items: center; gap: 10px; font-size: 19px; line-height: 1.3; margin-bottom: 8px; white-space: nowrap; }
  .contact .cap { font-size: 1.15em; }
  .contact svg { width: 20px; height: 20px; flex: none; fill: none; stroke: var(--light); stroke-width: 1.6; }
</style>
</head>
<body>
  <section class="card card--back" aria-label="Card back">
    <div class="brand"><span class="brand__mark"></span>Harbor Key Realty</div>
  </section>

  <section class="card card--front" aria-label="Card front">
    <div class="front__id">
      <div class="front__photo" role="img" aria-label="Headshot of Ray T. Dalworth"></div>
      <h1 class="front__name">Ray T. Dalworth</h1>
      <p class="front__title">Top Producer</p>
    </div>
    <div class="front__info">
      <div class="brand"><span class="brand__mark"></span>Harbor Key Realty</div>
      <ul class="contact">
        <li><svg viewBox="0 0 24 24"><path d="M6 3l4 4-2 3c1 2 4 5 6 6l3-2 4 4-3 3C10 20 4 14 3 6z"/></svg>313-482-6157</li>
        <li><svg viewBox="0 0 24 24"><rect x="3" y="6" width="18" height="12"/><path d="M3 6l9 7 9-7"/></svg>dalworth.ray.t@mailnest.example</li>
        <li><svg viewBox="0 0 24 24"><circle cx="12" cy="12" r="9"/><path d="M3 12h18M12 3c-4 5-4 13 0 18M12 3c4 5 4 13 0 18"/></svg><span>www.<span class="cap">L</span>ist<span class="cap">L</span>akeshore<span class="cap">H</span>omes.example</span></li>
        <li><svg viewBox="0 0 24 24"><circle cx="12" cy="12" r="9"/><path d="M3 12h18M12 3c-4 5-4 13 0 18M12 3c4 5 4 13 0 18"/></svg><span>www.<span class="cap">F</span>ind<span class="cap">L</span>akeshore<span class="cap">H</span>omes.example</span></li>
      </ul>
    </div>
  </section>
</body>
</html>
```